Letterhead That Inspires Trust

Birchwell Deed Services, LLC, (BDS) fixes technical problems with property deeds. The problems usually surface when someone tries to buy, sell or mortgage a piece of real estate and one of the lawyers involved find a title defect (a lien, an undischarged mortgage, a deceased person still on the title, unpaid taxes, etc.). BDS then gets involved and often has to contact prior property owners to get them to sign paperwork fixing the problem. We need a letterhead that will a) convey the seriousness of what we are trying to do, b) cause the recipients of our letters to recognize the importance of what are trying to do, and c) convey that we are a established and trustworthy company. We want it to include an image that suggests we are a problem solving company. Attached is an image we think might work; you can use it or not. In addition to our name (Birchwell Deed Services, LLC), the letterhead must include our address and phone number: 418 Calder Avenue, Suite 207, Providence, RI 02917 (401) 555-0372. We are thinking something straightforward without unnecessary colors or graphics.

```html
<!DOCTYPE html>
<html lang="en">
<head>
<meta charset="UTF-8">
<title>Birchwell Deed Services, LLC — Letterhead</title>
<link rel="stylesheet" href="https://fonts.googleapis.com/css2?family=Open+Sans:wght@400;600;700&display=swap">
<style>
  :root {
    --backdrop: #b1b3b1;
    --paper: #fafafa;
    --ink: #6b6b6b;
    --ink-dark: #333333;
    --brand-green: #009444;
    --band-dark: #2b2b2b;
    --signature-blue: #1a8fd0;
  }
  * { margin: 0; padding: 0; box-sizing: border-box; }
  html, body {
    width: 1200px; height: 950px; overflow: hidden;
    background: var(--backdrop);
    font-family: "Open Sans", Arial, sans-serif;
  }
  .letterhead {
    position: absolute; left: 306px; top: 58px;
    width: 589px; height: 833px;
    background: var(--paper);
    overflow: hidden;
  }
  .brand {
    position: absolute; left: 58px; top: 45px;
    display: flex; align-items: center; gap: 9px;
  }
  .brand-mark {
    width: 16px; height: 16px; background: var(--brand-green);
  }
  .brand-name {
    font-weight: 600; font-size: 21px; color: var(--brand-green);
    letter-spacing: 0.2px;
  }
  .letter-body {
    position: absolute; left: 58px; top: 204px; width: 473px;
    font-size: 8.6px; line-height: 15.1px; color: var(--ink);
  }
  .salutation { margin-bottom: 30px; }
  .letter-body p.copy { text-align: justify; margin-bottom: 14.5px; }
  .sign-off {
    position: absolute; left: 58px; top: 564px;
    font-size: 8.6px; color: var(--ink);
  }
  .sender-label { font-weight: 700; }
  .signature {
    display: block; margin: 10px 0 6px;
    width: 144px; height: 32px;
  }
  .footer-contact {
    position: absolute; left: 34px; top: 768px;
    color: var(--ink-dark); font-size: 10.8px; line-height: 18px;
    white-space: nowrap;
  }
  .contact-line { display: flex; align-items: center; gap: 4px; }
  .contact-item { display: inline-flex; align-items: center; gap: 5px; margin-right: 7px; }
  .contact-icon { width: 11px; height: 11px; }
  .footer-band {
    position: absolute; left: 0; bottom: 0; width: 589px; height: 22px;
  }
</style>
</head>
<body>
  <main class="letterhead">
    <header class="brand">
      <span class="brand-mark"></span>
      <span class="brand-name">Birchwell Deed Services, LLC</span>
    </header>

    <section class="letter-body">
      <p class="salutation">Dear Sir,</p>
      <p class="copy">Lorem Ipsum is simply dummy text of the printing and typesetting industry. Lorem Ipsum has been the industry's standard dummy text ever since the 1500s, when an unknown printer took a galley of type and scrambled it to make a type specimen book. It has survived not only five centuries, but also the leap into electronic typesetting, remaining essentially unchanged. It was popularised in the 1960s with the release of Marlowe sheets containing Lorem Ipsum passages, and more recently with desktop publishing software like Vellum PageForge including versions of Lorem Ipsum.</p>
      <p class="copy">Lorem Ipsum is simply dummy text of the printing and typesetting industry. Lorem Ipsum has been the industry's standard dummy text ever since the 1500s, when an unknown printer took a galley of type and scrambled it to make a type specimen book. It has survived not only five centuries, but also the leap into electronic typesetting, remaining essentially unchanged. It was popularised in the 1960s with the release of Marlowe sheets containing Lorem Ipsum passages, and more recently with desktop publishing software like Vellum PageForge including versions of Lorem Ipsum.</p>
      <p class="copy">Lorem Ipsum is simply dummy text of the printing and typesetting industry. Lorem Ipsum has been the industry's standard dummy text ever since the 1500s, when an unknown printer took a galley of type and scrambled it to make a type specimen book.</p>
    </section>

    <section class="sign-off">
      <p class="sender-label">Your Name</p>
      <svg class="signature" role="img" aria-label="Handwritten signature of the sender" viewBox="0 0 144 32">
        <rect x="0" y="4" width="144" height="24" rx="4" fill="var(--signature-blue)" opacity="0.18"/>
      </svg>
      <p class="sender-title">CEO &nbsp;|&nbsp; Owner</p>
    </section>

    <footer class="footer-contact">
      <p class="address">418 Calder Avenue, Suite 207, Providence, RI 02917</p>
      <p class="contact-line">
        <span class="contact-item">
          <svg class="contact-icon" viewBox="0 0 12 12" aria-hidden="true"><circle cx="6" cy="6" r="5.3" fill="none" stroke="var(--brand-green)" stroke-width="1.2"/><path d="M3.6 5.2 Q6 3.4 8.4 5.2 L8 6 L7 5.6 L7 5.1 Q6 4.7 5 5.1 L5 5.6 L4 6 Z M4.3 6.4 H7.7 L8 8.4 H4 Z" fill="var(--brand-green)"/></svg>
          (401) 555-0372
        </span>
        <span class="contact-item">
          <svg class="contact-icon" viewBox="0 0 12 12" aria-hidden="true"><circle cx="6" cy="6" r="5.3" fill="none" stroke="var(--brand-green)" stroke-width="1.2"/><rect x="3.3" y="4.2" width="5.4" height="3.8" fill="var(--brand-green)"/><path d="M3.3 4.2 L6 6.3 L8.7 4.2" fill="none" stroke="var(--paper)" stroke-width="0.7"/></svg>
          mail@birchwell.com
        </span>
        <span class="contact-item">
          <svg class="contact-icon" viewBox="0 0 12 12" aria-hidden="true"><circle cx="6" cy="6" r="5.3" fill="none" stroke="var(--brand-green)" stroke-width="1.2"/><circle cx="6" cy="6" r="2.9" fill="var(--brand-green)"/><path d="M3.1 6 H8.9 M6 3.1 V8.9" stroke="var(--paper)" stroke-width="0.6"/></svg>
          www.birchwell.com
        </span>
      </p>
    </footer>

    <svg class="footer-band" viewBox="0 0 589 22" preserveAspectRatio="none" aria-hidden="true">
      <rect x="0" y="11" width="589" height="11" fill="var(--band-dark)"/>
      <path d="M418 22 Q432 1 450 1 H589 V22 Z" fill="var(--brand-green)"/>
    </svg>
  </main>
</body>
</html>
```